Subway/Bus ad sign for a paid research study

We are looking for someone who can help design an effective advertisement sign for a paid research study. The ad will be displayed in subway stations/bus. The study involves fMRI and is conducted by a laboratory in the Calder Valley University.

We prefer ppt images so we could edit. Dimensions should be 46”h x 60”w, but may vary in the final version depending on our needs.

The way we would like to choose the final design is by running a pretest on plumfeed to pick the most attractive ad. Your submission would mean that you consent with this process.

Thank you for your consideration.

Target Market(s)

age 18-64, philadelphia

Requirements
Must have
• The ad must include the following information (we encourage you to come up with better/more catchy slogans)
• - We are looking for participants for a research study
• - This fMRI study is conducted by researchers at Calder Valley University
• - Email CvuCV2@lab.cvu-mail.org to see if you are eligible
• - Calder Valley University Logo
• The ad may include the following information
• - Participants get paid up to $190
Nice to have
• original attractive illustrations are highly encouraged.
Should not have
• It seems like brain photos tend to scare people away. Maybe you could focus on using survey-related images or illustrated images of the brain (vs. fMRI scans).

```html
<!DOCTYPE html>
<html lang="en">
<head>
<meta charset="utf-8">
<title>Active Mind – fMRI Study Poster</title>
<link href="https://fonts.googleapis.com/css2?family=Alfa+Slab+One&family=Arvo:wght@700&family=Didact+Gothic&display=swap" rel="stylesheet">
<style>
  :root {
    --page-bg: #e6e9ed;
    --frame: #8fa9c7;
    --ink-black: #050507;
    --cell-pink: #f06aa8;
    --cell-blue: #7fc4f0;
    --cell-violet: #a98be0;
    --glow-red: #ff2a2a;
    --text-white: #ffffff;
    --text-dark: #1b1b22;
    --brand-navy: #1c2458;
  }
  html, body {
    margin: 0;
    width: 1200px;
    height: 962px;
    overflow: hidden;
    background: var(--page-bg);
  }
  .poster {
    position: absolute;
    left: 289px;
    top: 31px;
    width: 622px;
    height: 900px;
    box-sizing: border-box;
    border: 12px solid var(--frame);
    background: var(--ink-black);
    overflow: hidden;
    font-family: "Didact Gothic", sans-serif;
  }
  .nerve-cell-art {
    position: absolute;
    inset: 0;
    background:
      radial-gradient(circle at 44% 3%, var(--glow-red) 0, rgba(255,42,42,0) 11%),
      radial-gradient(circle at 3% 72%, var(--glow-red) 0, rgba(255,42,42,0) 10%),
      radial-gradient(ellipse at 50% 55%, var(--cell-blue) 0, var(--cell-violet) 28%, var(--cell-pink) 44%, rgba(127,196,240,0.55) 60%, rgba(5,5,7,0) 78%),
      var(--ink-black);
  }
  .caption {
    position: absolute;
    left: 12px;
    top: 12px;
    font-size: 11px;
    color: var(--text-white);
    opacity: 0.85;
  }
  .headline {
    position: absolute;
    right: 72px;
    top: 272px;
    text-align: right;
    color: var(--text-white);
    line-height: 1;
  }
  .headline .lead {
    display: block;
    text-align: left;
    font-family: "Arvo", serif;
    font-weight: 700;
    font-size: 36px;
    margin-left: -30px;
  }
  .headline .big {
    display: block;
    font-family: "Alfa Slab One", serif;
    font-size: 78px;
    line-height: 0.78;
  }
  .headline .mid {
    display: block;
    font-family: "Alfa Slab One", serif;
    font-size: 58px;
    line-height: 0.95;
  }
  .invite {
    position: absolute;
    right: 72px;
    top: 436px;
    text-align: right;
    font-size: 28px;
    line-height: 1.18;
    color: var(--text-dark);
  }
  .contact {
    position: absolute;
    left: 0;
    right: 0;
    top: 543px;
    text-align: center;
    font-size: 21px;
    line-height: 1.22;
    color: var(--text-dark);
    padding-left: 6px;
  }
  .brand {
    position: absolute;
    left: 100px;
    top: 650px;
    display: flex;
    align-items: center;
    gap: 14px;
  }
  .brand-square {
    width: 86px;
    height: 86px;
    background: var(--brand-navy);
  }
  .brand-name {
    font-size: 32px;
    line-height: 1.05;
    color: var(--brand-navy);
  }
  .credit {
    position: absolute;
    left: 0;
    right: 0;
    top: 784px;
    text-align: center;
    font-size: 17px;
    line-height: 1.25;
    color: var(--text-white);
  }
  .location {
    position: absolute;
    right: 12px;
    bottom: 14px;
    font-size: 18px;
    color: var(--text-white);
  }
</style>
</head>
<body>
  <main class="poster">
    <div class="nerve-cell-art" role="img" aria-label="3D rendered nerve cell with glowing pink and blue branching dendrites on black"></div>
    <p class="caption" style="margin:0">3D rendered ‘nerve cell’</p>

    <h1 class="headline" style="margin:0">
      <span class="lead">Have an</span>
      <span class="big">active</span>
      <span class="mid">mind?</span>
    </h1>

    <p class="invite" style="margin:0">come and participate in a<br>fMRI research study</p>

    <p class="contact" style="margin:0">Email CvuCV2@lab.cvu-mail.org<br>to see if you are eligible</p>

    <div class="brand">
      <div class="brand-square"></div>
      <div class="brand-name">Calder Valley<br>University</div>
    </div>

    <p class="credit" style="margin:0">This study is conducted by researchers<br>at Calder Valley University</p>

    <p class="location" style="margin:0">Calder Valley, CV 20417</p>
  </main>
</body>
</html>
```